Relaunch website https://dancepastdawn.de/

We are looking for creative minds to relaunch the website for our new musical “Dance past dawn” (www.dancepastdawn.de). The aim is to convey the full emotional power, spine-tingling intensity, and spirit of empowerment of this unique production.

The site should make the emotional depth and power of the musical come to life - not merely by describing it, but by letting people feel it. In accordance with our marketing philosophy: "Show, don't tell"—we tell the story, rather than simply promoting the musical.

The website should be responsive, offer intuitive navigation and be in accordance with the design guidelines. Please design the website with the compatibility of a specific WordPress theme in mind (in the best case choose from a big enterprise theme such as avada, enfold or divi).

Design specifications:
Primary color: Pink (R224 / G51 / B151)
Secondary color: yellow (R255 / G221 / B0)
Tertiary color: black (R29 / G29 / B27)
Font-Headline: Tungsten
Font body: DIN 1451 LT Pro
Background texture: Grunge

In addition to the main page, the following subpages will be relevant:
OURtale, The Musical, Cast & Team, Tickets, Plan your visit, Corporate events, Press, FAQ, Coupon, News

The winner will be selected according to the following criteria: creativity, user guidance, technical feasibility and compliance with the style guide. Also based on your unique ideas! We know the briefing is super specific but please let your ideas and feedback flow.

We have uploaded a detailed briefing document (including the CI) in German and English as well as the logos. You can use all available graphics from the current website and socials if needed for your pitch. Please design at least the following pages:
- Home (briefing included)
- OURTale (be creative - no specific briefing)
- Ticketing (separate briefing included)
- Corporate events (separate briefing included)
- Plan your visit (separate briefing included)
- News (be creative - no specific briefing)

If you have any questions, please contact marla.fenwick@dosuvel-entertainment.

We would love to give you more time for your designs!

Target Market(s)

Germany

Industry/Entity Type

Musical & Entertainment

Number of Pages Required

5+ page

Font styles to use
Other font styles liked:
• Headline: Tungsten & Body: DIN 1451 LT Pro

Colors
FFF300
FFF600
FEFA6F
FFFEC7
FFFEE8
E54698
E96AAD
F1A4CE
F9D9EA
FCEFF6

Requirements
Must have
• See briefing
Nice to have
• See briefing
Should not have
• See briefing

```html
<!DOCTYPE html>
<html lang="de">
<head>
<meta charset="utf-8">
<title>Dance past dawn – Das Musical</title>
<link rel="stylesheet" href="https://fonts.googleapis.com/css2?family=Bungee&family=Bebas+Neue&family=Barlow:wght@400;500;600;700&display=swap">
<style>
:root{
  --pink:#e03397;
  --pink-soft:#f1a4ce;
  --magenta:#e60fb8;
  --yellow:#ffdd00;
  --yellow-soft:#fff36b;
  --ink:#1d1d1b;
  --cyan:#13d8e8;
  --lilac:#d8a8f0;
  --mint:#b5ebd6;
  --cream:#fff6e4;
  --display:"Bungee", "Impact", sans-serif;
  --condensed:"Bebas Neue", "Arial Narrow", sans-serif;
  --body:"Barlow", "Helvetica Neue", Arial, sans-serif;
}
*{box-sizing:border-box;margin:0;padding:0}
html,body{width:1200px;height:5263px;overflow:hidden}
body{font-family:var(--body);color:var(--ink);background:var(--cream);position:relative}
section,header,footer{position:absolute;left:0;width:1200px;overflow:hidden}
.abs{position:absolute}
.tag{position:absolute;display:inline-block;background:#fff;border:2px solid var(--ink);border-radius:20px;font:700 10px/1 var(--body);letter-spacing:.06em;text-transform:uppercase;padding:5px 10px;white-space:nowrap}
.box{border:3px solid var(--ink);border-radius:18px;box-shadow:7px 7px 0 var(--ink)}
.btn{position:absolute;display:flex;align-items:center;justify-content:center;border:2px solid var(--ink);border-radius:30px;box-shadow:4px 4px 0 var(--ink);font:700 13px/1 var(--body);white-space:nowrap}
h1,h2,h3{font-family:var(--display);font-weight:400;text-transform:uppercase}
.p{font-size:14px;line-height:1.7;color:#3b3b38}

.hero{top:0;height:944px;background:linear-gradient(180deg,#18d7ec 0%,#7fd0ec 18%,#d7a7ef 42%,#f4b7c6 60%,#ffd63a 80%,#ffdb1e 100%)}
.logo{position:absolute;font:400 28px/1 var(--condensed);color:#fff;letter-spacing:.02em;display:flex;align-items:center;gap:8px}
.logo i{display:block;width:12px;height:12px;background:#fff;border-radius:50%}
.logo small{font:600 9px/1 var(--body);letter-spacing:.3em;display:block;margin-top:2px}
.nav{position:absolute;left:468px;top:52px;display:flex;gap:22px;font:600 12px/1 var(--body);color:#fff}
.hero h1{position:absolute;left:96px;top:200px;font-size:72px;line-height:1.02;color:var(--ink)}
.outline{color:transparent;-webkit-text-stroke:2.5px var(--ink)}
.herblock{position:absolute;left:100px;top:436px;width:548px;height:166px;background:var(--pink);transform:rotate(-1.5deg);box-shadow:8px 8px 0 var(--ink);border-radius:6px;padding:14px 20px;font:400 70px/1.05 var(--display);color:#fff}
.card-back{position:absolute;left:715px;top:150px;width:390px;height:665px;background:var(--yellow);border:3px solid var(--ink);border-radius:26px;box-shadow:9px 9px 0 var(--ink);transform:rotate(2deg)}
.card-front{position:absolute;left:735px;top:150px;width:370px;height:340px;background:var(--pink);border:3px solid var(--ink);border-radius:24px;transform:rotate(-3deg);box-shadow:inset -16px -16px 0 #c98df0,7px 7px 0 var(--ink)}
.card-front .inner{position:absolute;left:22px;top:22px;right:26px;bottom:26px;background:var(--cream);border:3px solid var(--ink);border-radius:16px;padding:18px 20px}
.chip{display:inline-block;border-radius:10px;font:700 8px/1 var(--body);padding:5px 18px;text-transform:uppercase}

.marquee{top:944px;height:64px;background:var(--pink);display:flex;align-items:center;gap:40px;font:400 28px/1 var(--display);color:#fff3c4;white-space:nowrap}
.marquee .star{color:var(--yellow);font-size:24px}

.stats{top:1008px;height:586px;background:linear-gradient(100deg,#e6ec9e 0%,#c7e9b4 50%,#a8e8d2 100%)}
.stats h2{position:absolute;left:137px;top:128px;font-size:40px;line-height:1.25}
.hl{background:var(--yellow);padding:0 4px}
.stat{position:absolute;width:214px;height:120px;padding:18px 18px}
.stat b{display:block;font:400 44px/1 var(--display)}
.stat span{display:block;font:700 9px/1.3 var(--body);text-transform:uppercase;margin-top:14px}

.character{top:1594px;height:610px;background:linear-gradient(115deg,#f23ea2 0%,#e30fb5 55%,#d78ae9 100%)}
.ensemble{position:absolute;left:150px;top:88px;width:325px;height:460px;background:var(--cream);transform:rotate(-3deg)}
.character h2{position:absolute;left:599px;top:168px;font-size:50px;color:#fff}

.values{top:2204px;height:556px;background:linear-gradient(120deg,#e6c9ef 0%,#d6d8ea 50%,#bdeedd 100%)}
.values h2{position:absolute;left:0;width:1200px;text-align:center;top:136px;font-size:38px}
.value{position:absolute;top:243px;width:214px;height:185px;background:var(--cream);padding:22px 20px}
.value .ic{width:36px;height:36px;border:2px solid var(--ink);border-radius:50%;background:var(--yellow);display:flex;align-items:center;justify-content:center;margin-bottom:18px}
.value h3{font-size:17px;line-height:1.25;margin-bottom:10px}
.value p{font-size:11px;line-height:1.55;color:#555}

.reviews{top:2760px;height:506px;background:var(--cream)}
.reviews h2{position:absolute;left:123px;top:100px;font-size:36px}
.review{position:absolute;top:185px;width:298px;height:225px;padding:34px 30px}
.review .q{font:400 24px/1 var(--display)}
.review p{font-size:15px;line-height:1.65;margin:24px 0 12px}
.review cite{font:700 10px/1 var(--body);font-style:normal;text-transform:uppercase;letter-spacing:.04em}

.dates{top:3266px;height:612px;background:linear-gradient(180deg,#ffdc1e 0%,#fdbf3b 45%,#f86a86 80%,#f0489c 100%)}
.dates h2{position:absolute;left:137px;top:116px;font-size:50px;line-height:1.22}
.date{position:absolute;left:640px;width:425px;height:80px;background:var(--cream);display:flex;align-items:center;padding:0 18px;gap:16px}
.day{width:44px;height:48px;background:var(--pink);border:2px solid var(--ink);border-radius:10px;color:#fff;text-align:center;font:400 20px/1 var(--display);padding-top:6px}
.day small{display:block;font:700 7px/1 var(--body);margin-top:4px}
.date h3{font-size:15px}
.date .meta{font-size:10px;color:#777;margin-top:4px;letter-spacing:.05em}
.date .go{margin-left:auto;font:700 12px/1 var(--body)}

.venue{top:3878px;height:439px;background:linear-gradient(180deg,#f1dff0 0%,#ebd6eb 100%)}
.venue h2{position:absolute;left:137px;top:128px;font-size:40px;line-height:1}
.way{position:absolute;top:145px;width:168px;height:137px;background:var(--cream);text-align:center;padding:18px 10px}
.way .n{width:38px;height:38px;margin:0 auto 12px;border:2px solid var(--ink);border-radius:50%;background:var(--pink);color:#fff;font:400 16px/34px var(--display)}
.way h3{font-size:13px}
.way p{font-size:9px;color:#777;line-height:1.4;margin-top:6px}

.newsletter{top:4317px;height:446px;background:linear-gradient(180deg,var(--cream) 0%,var(--cream) 45%,#ef5d7e 58%,#e64387 100%)}
.nl-card{position:absolute;left:117px;top:98px;width:973px;height:323px;background:var(--yellow);overflow:hidden;border-radius:26px}
.nl-card h2{position:absolute;left:0;width:100%;text-align:center;top:72px;font:400 44px/1 var(--condensed)}
.field{position:absolute;left:44px;top:225px;width:589px;height:45px;background:#fff;border:2px solid var(--ink);border-radius:8px;padding:0 18px;display:flex;align-items:center;font-size:13px;color:#888}
.sub{position:absolute;left:647px;top:225px;width:168px;height:45px;background:var(--pink);border-radius:6px;color:#fff;display:flex;align-items:center;justify-content:center;font:400 16px/1 var(--condensed);letter-spacing:.08em}

.site-footer{top:4763px;height:500px;background:linear-gradient(180deg,#e63d89 0%,#ee5773 45%,#f69550 80%,#fbb640 100%);color:#fff}
.fcol{position:absolute;top:97px}
.fcol h4{font:400 17px/1 var(--condensed);letter-spacing:.08em;color:var(--yellow);margin-bottom:34px}
.fcol li{list-style:none;font-size:13px;line-height:2}
.soc{display:flex;gap:12px}
.soc span{width:34px;height:34px;border-radius:50%;background:#fff;display:block}
</style>
</head>
<body>

<header class="hero">
  <div class="logo" style="left:92px;top:40px"><i></i><div>DANCE PAST DAWN<small>DAS MUSICAL</small></div></div>
  <nav class="nav"><span>Home</span><span>OURtale</span><span>Corporate events</span><span>Corporate events</span><span>Plan your visit</span><span>News</span></nav>
  <div class="btn" style="left:968px;top:40px;width:136px;height:45px;background:var(--yellow);font:400 16px/1 var(--condensed);letter-spacing:.03em">TICKETS SICHERN</div>

  <span class="tag" style="left:96px;top:156px"><span style="color:var(--pink)">✳</span> Ein Musical über echte Heldinnen</span>
  <h1>Es ist<br>nicht<br><span class="outline">History.</span></h1>
  <div class="herblock">Es ist<br>OURtale.</div>
  <div class="abs" style="left:515px;top:198px;width:26px;height:26px;background:var(--yellow);border:2px solid var(--ink);transform:rotate(45deg)"></div>
  <div class="abs" style="left:642px;top:280px;width:56px;height:56px;background:var(--pink);border-radius:50%"></div>

  <p class="p abs" style="left:96px;top:622px;width:490px;font-size:14.5px">Neun Frauen. Ein Traum, der verboten war. Ein Sieg, der vergessen wurde. Win. Fight. Love. — wie eine Frau.</p>
  <div class="btn" style="left:96px;top:693px;width:200px;height:46px;background:var(--pink);color:#fff">Jetzt Tickets sichern →</div>
  <div class="abs" style="left:96px;top:777px;font:600 10px/1 var(--body);letter-spacing:.06em;display:flex;gap:14px">
    <span>★★★★★ PUBLIKUM</span><span>•</span><span>AB NOVEMBER 2026</span><span>•</span><span>HALLE 7 · KÖLN</span>
  </div>

  <div class="card-back"></div>
  <div class="card-front">
    <div class="inner">
      <div style="display:flex;justify-content:space-between;font:700 9px/1 var(--body);letter-spacing:.05em"><span>PREMIERE</span><span class="chip" style="background:var(--pink);color:#fff;padding:4px 10px">NO. 01</span></div>
      <div style="font:400 54px/1 var(--display);color:var(--pink);margin-top:20px">OUR</div>
      <div class="outline" style="font:400 54px/1 var(--display);-webkit-text-stroke:2px var(--ink)">TALE</div>
      <div style="display:flex;gap:14px;margin-top:14px">
        <span class="chip" style="background:var(--pink);color:#fff">Mut</span>
        <span class="chip" style="background:var(--cyan)">Liebe</span>
        <span class="chip" style="background:var(--yellow)">Sieg</span>
      </div>
      <p style="font-size:9px;line-height:1.5;color:#c03080;margin-top:18px">Inspiriert von einer wahren Geschichte aus dem Jahr 1971 — als neun Frauen die Welt zwangen, hinzusehen.</p>
    </div>
  </div>
  <div class="abs" style="left:1056px;top:142px;width:68px;height:68px;border-radius:50%;background:var(--yellow);border:2px solid var(--ink);font:700 9px/1.2 var(--body);display:flex;align-items:center;justify-content:center;text-align:center;transform:rotate(12deg)">NEU<br>2026</div>
</header>

<section class="marquee" aria-label="Laufband">
  <span>Win past dawn</span><span class="star">✷</span><span>Fight past dawn</span><span class="star">✷</span><span>Love past dawn</span>
</section>

<section class="stats">
  <span class="tag" style="left:137px;top:92px">Vergessene Geschichten · die die Welt verändern</span>
  <h2>1971 — die<br>Frauen, die<br><span class="hl">trotzdem</span><br>gespielt haben.</h2>
  <p class="p abs" style="left:137px;top:344px;width:470px;font-size:13.5px">Als der Verband sagte: „Frauen gehören nicht auf den Platz.“ — sagten sie: <b>„Doch.“</b> Sie reisten nach Mexiko, spielten vor 110.000 Zuschauer:innen und holten den Titel. Die Welt jubelte. Zuhause wurde geschwiegen.</p>
  <p class="p abs" style="left:137px;top:452px;width:470px;font-size:13.5px">Dieses Musical bringt ihre Stimmen, ihre Wut und ihre Liebe zurück auf die Bühne.</p>
  <div class="stat box" style="left:620px;top:172px;background:var(--cyan)"><b>9</b><span>Spielerinnen, ein Versprechen</span></div>
  <div class="stat box" style="left:850px;top:172px;background:var(--yellow)"><b>110K</b><span>Stimmen im Hauptstadion</span></div>
  <div class="stat box" style="left:620px;top:300px;background:var(--pink);color:#fff"><b>0</b><span>Mal in Schulbüchern erwähnt</span></div>
  <div class="stat box" style="left:850px;top:300px;background:var(--lilac)"><b>1</b><span>Bühne, die das ändert</span></div>
</section>

<section class="character">
  <div class="abs box" style="left:168px;top:78px;width:318px;height:460px;background:var(--yellow);transform:rotate(4deg)"></div>
  <div class="ensemble box">
    <div style="display:flex;justify-content:space-between;padding:18px 20px 0;font:700 8px/1 var(--body)"><span>ENSEMBLE · 01</span><span class="chip" style="background:var(--pink);color:#fff;padding:4px 10px">LEAD</span></div>
    <div role="img" aria-label="Porträtfläche der Figur Lotte" style="margin:12px 20px 0;height:280px;border:3px solid var(--ink);border-radius:16px;background:linear-gradient(180deg,#fbbd2c 0%,#f97a5e 55%,#f0489c 100%);display:flex;align-items:center;justify-content:center;font:400 46px/1 var(--display)">L</div>
    <div style="font:400 22px/1 var(--display);padding:18px 20px 8px">LOTTE</div>
    <div style="display:grid;grid-template-columns:1fr 1fr;gap:6px 8px;padding:0 20px">
      <span class="chip" style="background:var(--cyan);text-align:center">Mut</span>
      <span class="chip" style="background:var(--lilac);text-align:center">Solidarität</span>
      <span class="chip" style="background:var(--pink);color:#fff;text-align:center">Liebe</span>
      <span class="chip" style="background:var(--yellow);text-align:center">Sieg</span>
    </div>
  </div>
  <span class="tag" style="left:599px;top:120px;background:var(--magenta);color:#fff;border-color:#fff">Im Herzen der Geschichte</span>
  <h2>Lotte</h2>
  <div class="abs" style="left:599px;top:233px;font:600 10px/1 var(--body);letter-spacing:.05em;color:#ffd0ec">DIE STÜRMERIN, DIE NICHT AUFHÖREN WOLLTE.</div>
  <div class="abs" style="left:548px;top:278px;width:110px;height:50px;border-radius:50%;background:#9c1fa3;opacity:.7"></div>
  <p class="abs" style="left:599px;top:262px;width:460px;font-size:14px;line-height:1.7;color:#fff">Lotte ist 19. Sie liebt eine Frau, sie liebt das Spiel, und sie liebt die Welt, die ihr beides verbietet. Zwischen Küchentisch und Stadion findet sie eine Schwesternschaft, die stärker ist als jede Regel.</p>
  <p class="abs" style="left:599px;top:376px;width:460px;font-size:14px;line-height:1.6;color:#fff;font-weight:700">„Wir sind keine Mädchen, die spielen. Wir sind Frauen, die alles wagen.“</p>
  <div class="btn" style="left:599px;top:450px;width:284px;height:42px;background:var(--ink);color:#fff;border-color:#fff;box-shadow:none;font-size:12px;letter-spacing:.06em">LERNE DAS ENSEMBLE KENNEN →</div>
</section>

<section class="values">
  <span class="tag" style="left:478px;top:100px;font-size:9px">Ein Musical, das unter die Haut geht</span>
  <h2>Vier Worte. <span style="color:var(--pink)">Ein Versprechen.</span></h2>
  <div class="value box" style="left:137px"><div class="ic"><svg width="18" height="18" viewBox="0 0 18 18"><circle cx="9" cy="9" r="7" fill="none" stroke="#1d1d1b" stroke-width="1.6"/><path d="M6 11c1.5 1.5 4.5 1.5 6 0" fill="none" stroke="#1d1d1b" stroke-width="1.6"/></svg></div><h3>Mut</h3><p>Aufstehen, auch wenn dir gesagt wird, du gehörst nicht hierher.</p></div>
  <div class="value box" style="left:374px;height:210px"><div class="ic"></div><h3>Schwesternsc haft</h3><p>Neun Stimmen, ein Chor, der nicht mehr leiser wird.</p></div>
  <div class="value box" style="left:611px"><div class="ic" style="background:var(--pink)"><svg width="16" height="14" viewBox="0 0 16 14"><path d="M8 13 1.5 6.5A3.5 3.5 0 0 1 8 2a3.5 3.5 0 0 1 6.5 4.5Z" fill="#fff3" stroke="#1d1d1b" stroke-width="1.4"/></svg></div><h3>Liebe</h3><p>Lieben, wen man liebt. Offen. Laut. Ohne Entschuldigung.</p></div>
  <div class="value box" style="left:848px"><div class="ic">★</div><h3>Emotion</h3><p>Ein Abend, der dich umarmt, schüttelt und nicht mehr loslässt.</p></div>
</section>

<section class="reviews">
  <h2>Publikums-<span style="color:var(--pink)">Lieblinge</span></h2>
  <div class="btn" style="left:883px;top:87px;width:205px;height:48px;background:var(--pink);color:#fff">Jetzt Tickets sichern →</div>
  <div class="review box" style="left:110px;background:var(--cyan);transform:rotate(-1deg)"><div class="q">“</div><p>Ich habe geweint, gejubelt und am Ende meine Tochter umarmt. Dieses Stück gehört auf jede Bühne.</p><cite>— Nordstadt Zeitung</cite></div>
  <div class="review box" style="left:452px;background:var(--yellow);transform:rotate(1deg)"><div class="q">“</div><p>Pop, Power, Politik. Ein Musical, das endlich die Heldinnen feiert, die wir vergessen haben.</p><cite>— Radio Rheinwelle Kultur</cite></div>
  <div class="review box" style="left:792px;background:var(--lilac);transform:rotate(-.6deg)"><div class="q">“</div><p>Standing Ovations. Tränen. Und das Gefühl: Wir sind nicht allein.</p><cite>— Publikum, Premiere</cite></div>
</section>

<section class="dates">
  <span class="tag" style="left:137px;top:86px;font-size:9px">So verändern wir die Welt</span>
  <h2>Eine<br>Geschichte,<br><span style="background:var(--pink);color:#fff;padding:0 2px 0 120px">erzählt</span><br><span style="background:var(--pink);color:#fff">werden muss.</span></h2>
  <p class="p abs" style="left:137px;top:390px;width:470px;font-size:13.5px">Ab November 2026 — live, laut und unwiderstehlich in Halle 7, Köln. Komm allein, komm mit deiner Mutter, deiner Tochter, deiner besten Freundin. Komm einfach.</p>
  <div class="btn" style="left:137px;top:487px;width:160px;height:44px;background:var(--ink);color:#fff">Tickets ab 24 €</div>
  <div class="btn" style="left:303px;top:487px;width:176px;height:44px;background:var(--cream)">Gruppen &amp; Schulen</div>
  <div class="date box" style="top:118px"><div class="day">07<small>NOV</small></div><div><h3>Premiere</h3><div class="meta">HALLE 7 · KÖLN</div></div><span class="go" style="background:var(--yellow);border:2px solid var(--ink);border-radius:12px;padding:4px 10px;font-size:8px">WENIGE PLÄTZE</span></div>
  <div class="date box" style="top:211px"><div class="day">08<small>NOV</small></div><div><h3>Abendvorstellung</h3><div class="meta">HALLE 7 · KÖLN</div></div><span class="go">Tickets</span></div>
  <div class="date box" style="top:304px"><div class="day">14<small>NOV</small></div><div><h3>Matinee</h3><div class="meta">HALLE 7 · KÖLN</div></div><span class="go">Tickets</span></div>
  <div class="date box" style="top:397px"><div class="day">15<small>NOV</small></div><div><h3>Abendvorstellung</h3><div class="meta">HALLE 7 · KÖLN</div></div><span class="go">Tickets</span></div>
</section>

<section class="venue">
  <span class="tag" style="left:137px;top:96px;font-size:9px">So kommst du hin</span>
  <h2>Halle 7 ·<br><span style="color:var(--pink)">Drahtwerk<br>Köln</span></h2>
  <p class="p abs" style="left:137px;top:268px;width:380px;font-size:13.5px">Eine alte Fabrikhalle, frisch gestrichen mit Glitzer. Genau der richtige Ort für eine Geschichte, die laut werden muss.</p>
  <div class="way box" style="left:542px"><div class="n">1</div><h3>Mit der RSB</h3><p>Haltestelle Lindenhof, Linie 4 · 5 Min Fußweg</p></div>
  <div class="way box" style="left:720px"><div class="n">2</div><h3>Mit dem Rad</h3><p>Sichere Stellplätze direkt am Eingang</p></div>
  <div class="way box" style="left:898px"><div class="n">3</div><h3>Zu Fuß</h3><p>Aus Nordfeld in 15 Minuten erreichbar</p></div>
</section>

<section class="newsletter">
  <div class="nl-card box">
    <div class="abs" style="left:-30px;top:-40px;width:100px;height:110px;background:var(--cyan);border:3px solid var(--ink);border-radius:40%"></div>
    <div class="abs" style="left:880px;top:170px;width:140px;height:150px;background:var(--pink);border-radius:50%"></div>
    <h2>WERDE TEIL <span style="color:var(--pink)">DER BEWEGUNG</span></h2>
    <p class="abs" style="left:0;width:100%;text-align:center;top:150px;font-size:18px;line-height:1.45">Erhalten Sie exklusive Updates, Behind-the-Scenes-Inhalte<br>und 5% Rabatt auf Ihren ersten Ticketkauf</p>
    <div class="field">Geben Sie Ihre E-Mail ein</div>
    <div class="sub">ABONNIEREN</div>
  </div>
</section>

<footer class="site-footer">
  <div class="logo" style="left:157px;top:92px"><i></i><div>DANCE PAST DAWN<small>DAS MUSICAL</small></div></div>
  <p class="abs" style="left:157px;top:170px;width:200px;font-size:13px;line-height:1.4">Ein Musical über Mut, Emanzipation und die Kraft, den eigenen Weg zu gehen.</p>
  <div class="fcol" style="left:441px"><h4>SCHNELLZUGRIFF</h4><ul><li>Tickets</li><li>Die Geschichte</li><li>Cast &amp; Team</li><li>Spielort &amp; Anfahrt</li><li>Firmenevents</li><li>FAQ</li></ul></div>
  <div class="fcol" style="left:652px"><h4>KONTAKT</h4><ul>
    <li><svg width="11" height="11" viewBox="0 0 12 12" style="margin-right:8px"><path d="M2 1h3l1 3-2 1a7 7 0 0 0 3 3l1-2 3 1v3c-6 1-10-3-9-9Z" fill="none" stroke="var(--yellow)" stroke-width="1.3"/></svg>+49 221 555 0190</li>
    <li><svg width="11" height="9" viewBox="0 0 12 9" style="margin-right:8px"><rect x=".7" y=".7" width="10.6" height="7.6" fill="none" stroke="var(--yellow)" stroke-width="1.3"/><path d="M1 1l5 4 5-4" fill="none" stroke="var(--yellow)" stroke-width="1.3"/></svg>tickets@dancepastdawn.de</li></ul></div>
  <div class="fcol" style="left:916px"><h4>FOLGEN SIE UNS</h4><div class="soc"><span></span><span></span><span></span></div></div>
  <div class="abs" style="left:137px;top:366px;width:990px;height:1px;background:var(--yellow)"></div>
  <p class="abs" style="left:0;width:1200px;text-align:center;top:425px;font-size:13px">© 2026 Dance past dawn. Alle Rechte vorbehalten.</p>
</footer>

</body>
</html>
```